Global Expert Network Firm needs business card design

We need business card design for a new company based in Seoul, South Korea called 'Corwell Insight Partners'. We recruit industry experts covering all countries and connect our client and recruited expert by phone, face-to-face meetings and etc. We are a global expert network firm that is focused on delivering high-quality experts to our clients throughout the world. Our clients include multinational corporations, global consulting firms, private equity firms, venture capital firms, asset management companies.
We have made new logo and please find attachment.(Please use new logo)
Target Market(s)
Global Consulting Firms, Investment Firms, Private Equity Firms, Venture Capital Firms.
Industry/Entity Type
Recruitment
Contact Information for Business Card
We need two Languages (English and Korean Version).
The front is Korean and the back is English version.
[The back] [English]
Company Name: Corwell Insight Partners, Inc.
CEO Name: Daniel Park
Address: #507, Hanbit Bldg, 82 Maebongsan-ro, Dobong-gu, Seoul, 01327, Korea
Tel. +82 2 718 4052
Fax. +82 2 864 1097
Mobile. +82 10 7264 8815
Email: daniel@corwellip.com
Web: www.corwellip.com
[The front] [Korean] => Described in same order as English version.
회사명: 코웰인사이트파트너스(주)
대표이사: 박도현
주소: 서울시 도봉구 매봉산로 82 한빛빌딩 507호
Tel. 02 718 4052
Fax. 02 864 1097
Mobile. 010 7264 8815
Web: www.corwellip.com
Look and feel
Each slider illustrates characteristics of the customer's brand and the style your logo design should communicate.

```html
<!DOCTYPE html>
<html lang="en">
<head>
<meta charset="utf-8">
<title>Corwell Insight Partners — Business Cards</title>
<link href="https://fonts.googleapis.com/css2?family=Open+Sans:wght@400;600;700&family=Noto+Sans+KR:wght@400;500;700&display=swap" rel="stylesheet">
<style>
  :root {
    --backdrop: #e6e3df;
    --card: #f6f6f6;
    --card-shade: #e9e9e9;
    --navy: #1b2157;
    --band: #1a1a1a;
    --band-text: #e4e4e4;
    --ink: #141414;
    --muted: #4a4a4a;
    --icon: #5a63b0;
    --on-navy: #ffffff;
  }
  * { margin: 0; padding: 0; box-sizing: border-box; }
  html, body { width: 1200px; height: 832px; overflow: hidden; }
  body {
    background: var(--backdrop);
    font-family: "Open Sans", Arial, sans-serif;
    display: flex;
    flex-direction: column;
    align-items: center;
    justify-content: center;
    gap: 30px;
  }
  .card {
    position: relative;
    width: 660px;
    height: 367px;
    background: linear-gradient(135deg, var(--card) 0%, var(--card-shade) 100%);
    box-shadow: 0 10px 28px rgba(0,0,0,.22);
    overflow: hidden;
  }
  .logo-block {
    position: absolute;
    left: 395px;
    top: 22px;
    width: 228px;
    height: 170px;
    background: var(--navy);
    display: flex;
    align-items: center;
    justify-content: center;
    padding: 0 24px;
  }
  .company-name {
    color: var(--on-navy);
    font-family: "Open Sans", Arial, sans-serif;
    font-weight: 400;
    font-size: 18px;
    line-height: 1.4;
    text-align: center;
  }
  .website {
    position: absolute;
    left: 402px;
    top: 200px;
    font-size: 12px;
    font-weight: 600;
    letter-spacing: 3.5px;
    color: var(--ink);
  }
  .holder {
    position: absolute;
    left: 395px;
    top: 224px;
    display: flex;
    align-items: flex-start;
    gap: 9px;
  }
  .holder .dot {
    width: 13px; height: 13px;
    border-radius: 50%;
    background: var(--icon);
    margin-top: 5px;
  }
  .holder-name { font-size: 17px; font-weight: 700; color: var(--ink); line-height: 1.2; }
  .holder-title { font-size: 11px; color: var(--muted); }
  .band {
    position: absolute;
    left: 0; right: 0; bottom: 0;
    height: 94px;
    background: var(--band);
    display: flex;
    align-items: center;
    padding-left: 36px;
  }
  .contact {
    display: flex;
    gap: 8px;
    align-items: flex-start;
    color: var(--band-text);
    font-size: 12.5px;
    line-height: 1.6;
  }
  .contact.phones { width: 176px; }
  .contact.mail { width: 183px; }
  .contact .icons { display: flex; flex-direction: column; gap: 4px; padding-top: 3px; }
  .contact svg { width: 12px; height: 12px; fill: var(--icon); display: block; }
  .ko { font-family: "Noto Sans KR", "Open Sans", sans-serif; }
  .ko .holder-name { font-size: 17px; font-weight: 700; }
  .ko .contact.address { font-size: 12px; }
</style>
</head>
<body>

<section class="card card-english" aria-label="English side">
  <div class="logo-block"><p class="company-name">Corwell Insight Partners</p></div>
  <p class="website">www.corwellip.com</p>
  <div class="holder">
    <span class="dot"></span>
    <div><p class="holder-name">Daniel Park</p><p class="holder-title">CEO</p></div>
  </div>
  <div class="band">
    <div class="contact phones">
      <div class="icons">
        <svg viewBox="0 0 12 12"><path d="M3 1l2 2.5-1.2 1.2a7 7 0 003.5 3.5L8.5 7 11 9l-1.5 2C5 11 1 7 1 2.5z"/></svg>
        <svg viewBox="0 0 12 12"><rect x="3" y="0.5" width="6" height="11" rx="1"/></svg>
      </div>
      <div><p>+82 2 718 4052</p><p>+82 10 7264 8815</p></div>
    </div>
    <div class="contact mail">
      <div class="icons">
        <svg viewBox="0 0 12 12"><path d="M0.5 2h11v8h-11zM1.5 3l4.5 3.5L10.5 3z" fill-rule="evenodd"/></svg>
        <svg viewBox="0 0 12 12"><path d="M3 1h6v3H3zM1 5h10v5H9v1H3v-1H1z"/></svg>
      </div>
      <div><p>daniel@corwellip.com</p><p>+82 2 864 1097</p></div>
    </div>
    <div class="contact address">
      <div class="icons">
        <svg viewBox="0 0 12 12"><path d="M6 0.5a4 4 0 00-4 4c0 3 4 7 4 7s4-4 4-7a4 4 0 00-4-4zm0 2.5a1.5 1.5 0 110 3 1.5 1.5 0 010-3z" fill-rule="evenodd"/></svg>
      </div>
      <div><p>#507, Hanbit Bldg, 82 Maebongsan-ro,</p><p>Dobong-gu, Seoul, 01327, Korea</p></div>
    </div>
  </div>
</section>

<section class="card card-korean ko" aria-label="Korean side" lang="ko">
  <div class="logo-block"><p class="company-name">Corwell Insight Partners</p></div>
  <p class="website">www.corwellip.com</p>
  <div class="holder">
    <span class="dot"></span>
    <div><p class="holder-name">박도현</p><p class="holder-title">대표이사</p></div>
  </div>
  <div class="band">
    <div class="contact phones">
      <div class="icons">
        <svg viewBox="0 0 12 12"><path d="M3 1l2 2.5-1.2 1.2a7 7 0 003.5 3.5L8.5 7 11 9l-1.5 2C5 11 1 7 1 2.5z"/></svg>
        <svg viewBox="0 0 12 12"><rect x="3" y="0.5" width="6" height="11" rx="1"/></svg>
      </div>
      <div><p>+82 2 718 4052</p><p>+82 10 7264 8815</p></div>
    </div>
    <div class="contact mail">
      <div class="icons">
        <svg viewBox="0 0 12 12"><path d="M0.5 2h11v8h-11zM1.5 3l4.5 3.5L10.5 3z" fill-rule="evenodd"/></svg>
        <svg viewBox="0 0 12 12"><path d="M3 1h6v3H3zM1 5h10v5H9v1H3v-1H1z"/></svg>
      </div>
      <div><p>daniel@corwellip.com</p><p>+82 2 864 1097</p></div>
    </div>
    <div class="contact address">
      <div class="icons">
        <svg viewBox="0 0 12 12"><path d="M6 0.5a4 4 0 00-4 4c0 3 4 7 4 7s4-4 4-7a4 4 0 00-4-4zm0 2.5a1.5 1.5 0 110 3 1.5 1.5 0 010-3z" fill-rule="evenodd"/></svg>
      </div>
      <div><p>서울시 도봉구 매봉산로 82</p><p>한빛빌딩 507호</p></div>
    </div>
  </div>
</section>

</body>
</html>
```